High-end residential home builder needs a business card design

We need a new business card design for a small residential construction company based in Boise, Idaho. We specialize in building custom high-end homes and remodels, with a focus on great design and craftsmanship.

We would like to use our current logo, but open to new color suggestions.
Just looking for a clean, sharp, modern design that looks high-end.

Target Market(s)

Upscale clientele

Industry/Entity Type

Contractor

Contact Information for Business Card

Company: Stonefield Custom Builders
Name: Marcus Tilley
Phone number: 208 367 4120
Email: MarcusTilleySCB@mailbox-example.com
Website: Stonefieldcustombuilders-example.com

Font styles to use
Serif
Sans Serif

Requirements
Must have
• Company Logo
Company name
My name
My phone number
My email
Company website
Nice to have
• I have attached a few photos of cards that I really like.

```html
<!DOCTYPE html>
<html lang="en">
<head>
<meta charset="utf-8">
<title>Stonefield Custom Builders – Business Card</title>
<link rel="stylesheet" href="https://fonts.googleapis.com/css2?family=Raleway:wght@500;700&family=Roboto:wght@400&display=swap">
<style>
  :root {
    --canvas: #9a9a9a;
    --paper: #fbfbfa;
    --ink: #2e2624;
    --espresso: #2a1f17;
    --espresso-deep: #160f0a;
    --gold: #d9a04f;
    --grey-text: #4a4a4a;
  }
  * { box-sizing: border-box; margin: 0; padding: 0; }
  html, body { width: 1200px; height: 1022px; overflow: hidden; }
  body {
    background: var(--canvas);
    display: flex;
    flex-direction: column;
    align-items: center;
    justify-content: center;
    gap: 28px;
  }
  .card {
    position: relative;
    width: 820px;
    height: 469px;
    overflow: hidden;
  }

  /* Front */
  .card-front { background: var(--paper); }
  .brand {
    position: absolute;
    left: 58px;
    top: 168px;
    display: flex;
    align-items: center;
    gap: 22px;
  }
  .brand-mark {
    width: 64px;
    height: 64px;
    border: 3px solid var(--ink);
  }
  .brand-name {
    font-family: "Raleway", sans-serif;
    font-weight: 700;
    color: var(--ink);
    font-size: 22px;
    letter-spacing: 0.32em;
    text-transform: uppercase;
    border-bottom: 1.5px solid var(--ink);
    padding-bottom: 6px;
  }
  .brand-sub {
    font-family: "Raleway", sans-serif;
    font-weight: 500;
    color: var(--gold);
    font-size: 13px;
    letter-spacing: 0.42em;
    text-transform: uppercase;
    margin-top: 6px;
  }
  .divider {
    position: absolute;
    left: 400px;
    width: 2px;
    background: var(--ink);
  }
  .divider-top { top: 132px; height: 44px; }
  .divider-bottom { top: 200px; height: 84px; }
  .person {
    position: absolute;
    left: 428px;
    top: 140px;
  }
  .person-name {
    font-family: "Raleway", sans-serif;
    font-weight: 700;
    font-size: 24px;
    color: var(--ink);
    text-transform: uppercase;
  }
  .person-role {
    font-family: "Roboto", sans-serif;
    font-size: 19px;
    color: var(--gold);
  }
  .contact {
    position: absolute;
    left: 420px;
    top: 212px;
    list-style: none;
    font-family: "Roboto", sans-serif;
    font-size: 17.5px;
    color: var(--grey-text);
    line-height: 26px;
  }
  .contact li { display: flex; align-items: center; gap: 9px; }
  .contact svg { width: 16px; height: 16px; flex: none; }
  .edge-band {
    position: absolute;
    left: 0; right: 0; bottom: 0;
    height: 26px;
  }
  .edge-band-dark {
    position: absolute; inset: 0;
    background: var(--espresso);
    clip-path: polygon(0 0, 52% 0, 50% 100%, 0 100%);
  }
  .edge-band-gold {
    position: absolute; inset: 0;
    background: var(--gold);
    clip-path: polygon(53% 0, 100% 0, 100% 100%, 51% 100%);
  }

  /* Back */
  .card-back {
    background: linear-gradient(135deg, var(--espresso-deep), var(--espresso) 55%, var(--espresso-deep));
  }
  .back-pattern {
    position: absolute; inset: 0;
    background: radial-gradient(circle at 70% 40%, rgba(255,255,255,0.06), transparent 60%);
  }
  .back-badge {
    position: absolute;
    right: 110px;
    bottom: 92px;
    display: flex;
    align-items: center;
    gap: 10px;
  }
  .back-badge-mark {
    width: 22px; height: 22px;
    border: 2px solid var(--gold);
  }
  .back-badge-name {
    font-family: "Raleway", sans-serif;
    font-weight: 700;
    font-size: 16px;
    letter-spacing: 0.28em;
    color: #ffffff;
    text-transform: uppercase;
  }
</style>
</head>
<body>
  <section class="card card-front">
    <div class="brand">
      <div class="brand-mark"></div>
      <div class="brand-text">
        <div class="brand-name">Stonefield</div>
        <div class="brand-sub">Custom Builders</div>
      </div>
    </div>

    <div class="divider divider-top"></div>
    <div class="divider divider-bottom"></div>

    <div class="person">
      <div class="person-name">Marcus Tilley</div>
      <div class="person-role">Managing Director</div>
    </div>

    <ul class="contact">
      <li>
        <svg viewBox="0 0 16 16"><path d="M3 1.5l3 .5 1 3.5-2 1.2a8 8 0 0 0 4.3 4.3l1.2-2 3.5 1 .5 3c-6.5 1-12.5-5-11.5-11.5z" fill="var(--ink)"/></svg>
        208 367 4120
      </li>
      <li>
        <svg viewBox="0 0 16 16"><rect x="1" y="3" width="14" height="10" fill="none" stroke="var(--ink)" stroke-width="1.6"/><path d="M1 3l7 6 7-6" fill="none" stroke="var(--ink)" stroke-width="1.6"/></svg>
        MarcusTilleySCB@mailbox-example.com
      </li>
      <li>
        <svg viewBox="0 0 16 16"><circle cx="8" cy="8" r="6.5" fill="none" stroke="var(--ink)" stroke-width="1.4"/><ellipse cx="8" cy="8" rx="3" ry="6.5" fill="none" stroke="var(--ink)" stroke-width="1.2"/><path d="M1.5 8h13" stroke="var(--ink)" stroke-width="1.2"/></svg>
        Stonefieldcustombuilders-example.com
      </li>
    </ul>

    <div class="edge-band">
      <div class="edge-band-dark"></div>
      <div class="edge-band-gold"></div>
    </div>
  </section>

  <section class="card card-back">
    <div class="back-pattern" role="img" aria-label="Embossed repeating brand pattern on dark espresso stock"></div>
    <div class="back-badge">
      <div class="back-badge-mark"></div>
      <div class="back-badge-name">Stonefield</div>
    </div>
  </section>
</body>
</html>
```